Business Card Design Project

Build kick ass business card.
Updates

I just uploaded the Vorintex Logo in AI format, for those that were asking. It's looking real good and we'll be reviewing the designs soon. Thanks. 

Target Market(s)

Businesses in many verticals. Focusing on information security.

Vorintex, LLC
Gordon Bexley
Principal Security Consultant
Mobile: +1-602-555-0187
Email: Gordon.Bexley@Vorintex.example
Web: www.vorintex.example

Industry/Entity Type

Business

Requirements
Must have
• Design must look high-end, hi-tech stylish and minimalist

Be different – one that stands out from thousands of others

Does not have to be traditional rectangle

Would like logo integrated

```html
<!DOCTYPE html>
<html lang="en">
<head>
<meta charset="utf-8">
<title>Vorintex – Gordon Bexley</title>
<link rel="stylesheet" href="https://fonts.googleapis.com/css2?family=Fira+Sans+Condensed:wght@300;400;700&display=swap">
<style>
  :root {
    --paper: #ffffff;
    --ink-dark: #3a3a3a;
    --ink-light: #ffffff;
    --brand-blue: #2a9fd6;
    --band-blue: #5bbde0;
    --band-pale: #d5e9f1;
    --panel-top: #0c0c0c;
    --panel-bottom: #7d7d7d;
  }
  html, body {
    margin: 0;
    padding: 0;
    overflow: hidden;
    background: var(--paper);
  }
  .card {
    position: relative;
    width: 686px;
    height: 1200px;
    overflow: hidden;
    background: var(--paper);
    font-family: "Fira Sans Condensed", "Arial Narrow", sans-serif;
  }
  .band-pale {
    position: absolute;
    left: 0;
    right: 0;
    top: 470px;
    height: 330px;
    background: linear-gradient(180deg, var(--paper) 0%, var(--band-pale) 100%);
    clip-path: polygon(0 45%, 100% 0, 100% 100%, 0 100%);
  }
  .band-blue {
    position: absolute;
    left: 0;
    right: 0;
    top: 640px;
    height: 160px;
    background: var(--band-blue);
    clip-path: polygon(0 55%, 100% 0, 100% 100%, 0 100%);
  }
  .panel {
    position: absolute;
    left: 0;
    right: 0;
    top: 700px;
    bottom: 0;
    background: linear-gradient(180deg, var(--panel-top) 0%, var(--panel-bottom) 100%);
    clip-path: polygon(0 14%, 100% 0, 100% 100%, 0 100%);
  }
  .brand {
    position: absolute;
    left: 40px;
    top: 120px;
    display: flex;
    align-items: center;
    gap: 30px;
  }
  .brand-dot {
    width: 120px;
    height: 120px;
    border-radius: 50%;
    background: var(--brand-blue);
    flex: none;
  }
  .brand-text {
    display: flex;
    flex-direction: column;
  }
  .brand-name {
    font-size: 84px;
    font-weight: 400;
    color: var(--ink-dark);
    letter-spacing: 3px;
    line-height: 1;
  }
  .brand-tagline {
    margin-top: 6px;
    font-size: 28px;
    font-weight: 400;
    color: var(--ink-dark);
    letter-spacing: 1px;
    word-spacing: 6px;
    line-height: 1;
  }
  .contact {
    position: absolute;
    right: 70px;
    top: 818px;
    text-align: right;
    color: var(--ink-light);
    white-space: nowrap;
  }
  .contact-name {
    margin: 0 0 6px;
    font-size: 40px;
    font-weight: 700;
    line-height: 1.1;
  }
  .contact-line {
    margin: 0;
    font-size: 37px;
    font-weight: 300;
    line-height: 57px;
  }
</style>
</head>
<body>
<main class="card">
  <div class="band-pale" aria-hidden="true"></div>
  <div class="band-blue" aria-hidden="true"></div>
  <div class="panel" aria-hidden="true"></div>

  <header class="brand">
    <span class="brand-dot"></span>
    <span class="brand-text">
      <span class="brand-name">Vorintex</span>
      <span class="brand-tagline">network security solutions</span>
    </span>
  </header>

  <section class="contact">
    <p class="contact-name">Gordon Bexley</p>
    <p class="contact-line">Principal Security Consultant</p>
    <p class="contact-line">Mobile: +1-602-555-0187</p>
    <p class="contact-line">Email: Gordon.Bexley@Vorintex.example</p>
    <p class="contact-line">Web: www.vorintex.example</p>
  </section>
</main>
</body>
</html>
```